Brochure Design Template

We need a template design so we can add and change content as required.

The size is A4 Landscape (297mm X 210mm) divided into three individual DL sections (99mm X 210mm) that have their own individual color or look. This give us the option to print as DL or have three separate services offered on on brochure.

So who are we. We are a photographic service that in Australia that offers service from commercial photography, photography training, photographic studio hire as well as a photo booth.
Our website is brimlane.net.

We are after ideas that are modern and colorful and fits the look of our logo.. Please feel free to put questions or ideas to us..
Thanks kindly..
Updates

Target Market(s)

weddings and commerical businesses

Industry/Entity Type

Landscape

Requirements
Must have
• The size is A4 Landscape (297mm X 210mm) divided into three individual DL sections (99mm X 210mm) that have their own individual color or look. This give us the option to print as DL or have three separate services offered on on brochure.

Template is for use in Adobe indesign

```html
<!DOCTYPE html>
<html lang="en">
<head>
<meta charset="utf-8">
<title>Brimlane Photographic Services – DL Brochure Template</title>
<link href="https://fonts.googleapis.com/css2?family=Permanent+Marker&family=Architects+Daughter&family=Questrial&display=swap" rel="stylesheet">
<style>
:root{
  --page:#d9d9d9;
  --panel-top:#0f0f0f;
  --panel-bottom:#3a3a3a;
  --white:#ffffff;
  --red:#d7191c;
  --grey-box:#7a7c7e;
  --grey-light:#a7a9ab;
  --text-dark:#1b1b1b;
}
*{box-sizing:border-box;margin:0;padding:0}
html,body{width:1200px;height:1000px;overflow:hidden}
body{background:var(--page);font-family:"Questrial",sans-serif;position:relative}
.sheet{position:absolute;left:267px;display:flex;box-shadow:0 6px 18px rgba(0,0,0,.35)}
.sheet--front{top:22px}
.sheet--back{top:510px}
.panel{position:relative;width:222px;height:468px;overflow:hidden;
  background:linear-gradient(180deg,var(--panel-top) 0%,#222 55%,var(--panel-bottom) 100%);
  border-right:1px solid #555}
.panel:last-child{border-right:none}
.panel__title{position:absolute;top:12px;left:0;right:0;text-align:center;
  font-family:"Permanent Marker",cursive;font-weight:400;color:var(--white);font-size:23px;letter-spacing:.5px}
.frame{position:absolute;left:14px;right:14px;border-radius:14px}
.frame--outline{border:2px solid var(--white)}
.frame--grey{background:var(--grey-box);border:2px solid var(--white)}
.frame--red{background:var(--red);border:2px solid var(--white)}
.frame--paper{background:var(--white);border:2px solid #555;outline:2px solid var(--white);outline-offset:2px}
.photo{position:absolute;border:4px solid var(--white);border-radius:4px;box-shadow:0 2px 5px rgba(0,0,0,.5)}
.caption{position:absolute;font-family:"Architects Daughter",cursive;font-size:11px;color:var(--white);white-space:nowrap}
.caption--dark{color:var(--text-dark)}
.brand{position:absolute;left:18px;bottom:16px;display:flex;align-items:center;gap:9px}
.brand__dot{width:24px;height:24px;border-radius:50%;background:var(--red)}
.brand__name{font-family:"Questrial",sans-serif;font-size:24px;color:var(--white);letter-spacing:1px}
.copy{position:absolute;font-size:6.4px;line-height:1.3;color:var(--text-dark)}
.copy p{margin-bottom:5px}
.copy b{font-style:italic;font-size:7.4px}
.copy .lead{font-weight:700;font-size:8px;font-style:normal;line-height:1.25;margin-bottom:8px}
.copy--light{color:var(--white)}
.copy--light .lead{font-style:italic}
.call{position:absolute;border-radius:50%;display:flex;flex-direction:column;align-items:center;justify-content:center;
  text-align:center;color:var(--white);font-weight:700;font-size:8.5px;line-height:1.1}
.call span{font-weight:400;font-size:6.5px;margin-top:3px}
.call--red{background:var(--red);border:2px solid var(--white)}
.call--grey{background:var(--grey-light);border:2px solid var(--white)}
.offer{position:absolute;border-radius:50%;background:var(--white);color:var(--text-dark);text-align:center;
  display:flex;flex-direction:column;align-items:center;justify-content:center;padding:12px;box-shadow:0 2px 5px rgba(0,0,0,.4)}
.offer strong{font-size:8.5px;line-height:1.05}
.offer small{font-size:5.2px;line-height:1.25;margin-top:3px}
.facilities{list-style:none;margin-top:3px}
</style>
</head>
<body>

<section class="sheet sheet--front">
  <article class="panel panel--training">
    <h2 class="panel__title">TRAINING</h2>
    <div class="frame frame--outline" style="top:56px;height:358px"></div>
    <div class="photo" role="img" aria-label="Photographers shooting a mountain valley" style="left:28px;top:72px;width:170px;height:92px;background:linear-gradient(160deg,#8ba56a,#3f5a3a 60%,#1e2a33)"></div>
    <div class="caption" style="left:28px;top:168px">Lighting ...</div>
    <div class="photo" role="img" aria-label="Student photographing rock formation with lighting" style="left:30px;top:184px;width:140px;height:100px;transform:rotate(-4deg);background:linear-gradient(130deg,#d9c4a0,#7a4a28 55%,#2a1e16)"></div>
    <div class="caption" style="left:150px;top:284px">SLR ...</div>
    <div class="photo" role="img" aria-label="Silhouette of a photographer with tripod at dusk" style="left:84px;top:302px;width:122px;height:94px;background:linear-gradient(180deg,#5d6d7e,#2c3440 65%,#111)"></div>
    <div class="brand"><span class="brand__dot"></span><span class="brand__name">BRIMLANE</span></div>
  </article>

  <article class="panel panel--photography">
    <h2 class="panel__title">PHOTOGRAPHY</h2>
    <div class="frame frame--grey" style="top:56px;height:358px"></div>
    <div class="photo" role="img" aria-label="Real estate homestead with green lawn" style="left:20px;top:52px;width:176px;height:94px;transform:rotate(2deg);background:linear-gradient(180deg,#9fc2e0,#c9b48a 45%,#4f8a2f)"></div>
    <div class="caption caption--dark" style="left:96px;top:128px">Real Estate ...</div>
    <div class="caption" style="left:20px;top:160px">Commercial ...</div>
    <div class="photo" role="img" aria-label="Event group photo in front of a rescue helicopter" style="left:24px;top:177px;width:172px;height:90px;background:linear-gradient(180deg,#c8ccd2,#e6b52e 40%,#c43a2a 70%,#3a5aa8)"></div>
    <div class="caption" style="left:22px;top:269px">Events ...</div>
    <div class="caption" style="left:130px;top:269px">Portraiture ...</div>
    <div class="photo" role="img" aria-label="Corporate portrait" style="left:22px;top:286px;width:176px;height:98px;background:linear-gradient(110deg,#d8cfa8,#a89a6e 55%,#2a2a2a)"></div>
    <div class="caption" style="left:28px;top:386px">Landscape ...</div>
    <div class="brand"><span class="brand__dot"></span><span class="brand__name">BRIMLANE</span></div>
  </article>

  <article class="panel panel--studio">
    <h2 class="panel__title">STUDIO HIRE</h2>
    <div class="frame frame--red" style="top:56px;height:358px"></div>
    <div class="photo" role="img" aria-label="Studio portrait with novelty props" style="left:34px;top:52px;width:150px;height:94px;transform:rotate(-3deg);background:linear-gradient(135deg,#e9e4dc,#c8a57a 55%,#333)"></div>
    <div class="photo" role="img" aria-label="Make-up artist at work in the studio" style="left:72px;top:152px;width:130px;height:80px;background:linear-gradient(135deg,#5a3a2a,#b77c5a 50%,#1a1a1a)"></div>
    <div class="caption" style="left:112px;top:238px">Space ...</div>
    <div class="photo" role="img" aria-label="Woman in a green dress in a forest" style="left:20px;top:228px;width:80px;height:146px;transform:rotate(-2deg);background:linear-gradient(180deg,#3e4a34,#2f6b3a 50%,#1d2a1d)"></div>
    <div class="photo" role="img" aria-label="Black photo booth kiosk" style="left:110px;top:264px;width:56px;height:142px;border-width:0;background:linear-gradient(90deg,#111,#333 60%,#0a0a0a)"></div>
    <div class="photo" role="img" aria-label="Strip of photo booth prints" style="left:172px;top:262px;width:34px;height:132px;border-width:3px;background:linear-gradient(180deg,#6a8a4a,#b08a60 35%,#4a6a9a 65%,#7aa04a)"></div>
    <div class="caption" style="left:22px;top:384px">Photo Booth ...</div>
    <div class="brand"><span class="brand__dot"></span><span class="brand__name">BRIMLANE</span></div>
  </article>
</section>

<section class="sheet sheet--back">
  <article class="panel panel--training">
    <h2 class="panel__title">TRAINING</h2>
    <div class="frame frame--paper" style="top:56px;height:350px"></div>
    <div class="copy" style="left:26px;top:70px;width:170px">
      <p class="lead" style="width:112px">Enrol in the most comprehensive digital photography course designed for beginners by pro photographers!</p>
      <p><b>SLR Photography Courses</b> - SLR photography courses are designed for those who are new to the digital SLR photography world and want to get professional looking images from their new camera.</p>
      <p><b>Flashgun Workshop</b> - The flashgun workshop is designed for those who have bought a flash but can't understand how to get the most from it.</p>
      <p><b>Studio Workshop</b> - This studio workshop will unravel the mystery behind using strobe lighting within a studio environment and let you take control of studio lighting conditions.</p>
      <p><b>Darkroom Pro 4 Tutorial</b> - This tutorial training package has been designed for those who are new to Darkroom Pro. These are simple short videos designed to guide the user through each process required to use Darkroom Pro 4.</p>
    </div>
    <div class="call call--red" style="left:148px;top:62px;width:54px;height:54px">Call<br>Today!<span>02-5550<br>0196</span></div>
    <div class="brand"><span class="brand__dot"></span><span class="brand__name">BRIMLANE</span></div>
  </article>

  <article class="panel panel--photography">
    <h2 class="panel__title">PHOTOGRAPHY</h2>
    <div class="frame frame--grey" style="top:56px;height:350px"></div>
    <div class="copy" style="left:26px;top:70px;width:168px">
      <p class="lead" style="font-style:italic">Brimlane Photographic Services provides unique event, corporate, portraiture, architecture and landscape photography services across New South Wales</p>
      <p><b>Commercial</b> - Covering corporate, staff and business promotion.</p>
      <p><b>Events</b> - Including open days, sports, shows, parties and media promotions.</p>
      <p><b>Elevated Photography</b> - Twenty metre photography platform to cover the aerial perspective.</p>
      <p><b>Real Estate</b> - From home owners to real estate agents to property developers and rural properties.</p>
      <p><b>Portraiture</b> - Beautiful portraits are created within our two professional studios or on location.</p>
      <p><b>Landscape</b> - Architecture.</p>
      <p><b>Fine Art</b> - Can be<br>commission upon request.</p>
    </div>
    <div class="call call--red" style="left:150px;top:322px;width:54px;height:54px">Call<br>Today!<span>02-5550<br>0196</span></div>
    <div class="brand"><span class="brand__dot"></span><span class="brand__name">BRIMLANE</span></div>
  </article>

  <article class="panel panel--studio">
    <h2 class="panel__title">STUDIO HIRE</h2>
    <div class="frame frame--red" style="top:56px;height:322px"></div>
    <div class="copy copy--light" style="left:26px;top:68px;width:172px">
      <p class="lead">Brimlane has a unique fully equipped studio space that can be hired. The space is ideal for portraits that can be captured with a white seamless background or one of other eight backdrops available for use</p>
      <p><b>The Facilities Include</b></p>
      <ul class="facilities">
        <li>- Three studio lights on tripods or booms</li>
        <li>- Lighting accessories</li>
        <li>- Numerous backdrops to use</li>
        <li>- Access to two studio spaces</li>
        <li>- Coffee/tea facilities</li>
        <li>- Make up and change room facilities</li>
      </ul>
    </div>
    <div class="photo" role="img" aria-label="Portrait session on a studio set" style="left:22px;top:248px;width:92px;height:86px;background:linear-gradient(135deg,#b9b9b9,#4a4a4a 55%,#1a1a1a)"></div>
    <div class="offer" style="left:110px;top:240px;width:100px;height:100px">
      <strong>We also offer<br>PHOTO BOOTH<br>HIRE!</strong>
      <small>The photo booth is the perfect addition for your wedding, party or corporate event</small>
      <small><b>Call Today!</b></small>
    </div>
    <div class="call call--grey" style="left:72px;top:340px;width:56px;height:56px">Call<br>Today!<span>02-5550<br>0196</span></div>
    <div class="brand"><span class="brand__dot"></span><span class="brand__name">BRIMLANE</span></div>
  </article>
</section>

</body>
</html>
```